VEK.PRO- Daniel Whitcombe Fitness- needs a clever business card using the logo, name, info, contact

I need a business card designed for my Online Personal Training company called VEK.PRO, abbreviation for Daniel Whitcombe Fitness. My company focuses on coaching in personal health and personal growth to unleash your greatest potential. I would like to see designs that use my color scheme of a redish-orange (C:0,M:84,Y:100,K:0), grey, white, black, and my company font is OSWALD. The final design should communicate some aspects of design, health, motivation, growth, in some way. The logo is very important to the company and can be displayed in any of the colors previously mentioned. Must include the company name, my website: www.vek.example , my email: dan@vek.example

Target Market(s)

Personal health, fitness, general public, those who lack knowledge, awareness, and confidence in personal health

Industry/Entity Type

Personal Trainer

Font styles to use
Other font styles liked:
• OSWALD. (Bold, Regular, Light)

Colors
f37122
ffffff
9d9d9d
000000

Requirements
Must have
• Must include the logo, company name, my website: www.vek.example , my email: dan@vek.example
Nice to have
• Variations of the colors scheme of a redish-orange (C:0,M:84,Y:100,K:0), grey, white, black. Logo, card, or text can be in any of these colors.
• Possible quote like "Take control of your personal health to unleash your greatest potential" or "Unleashing your greatness first begins with fitness of the body and mind"

```html
<!DOCTYPE html>
<html lang="en">
<head>
<meta charset="utf-8">
<title>VEK.PRO Business Card</title>
<link rel="stylesheet" href="https://fonts.googleapis.com/css2?family=Oswald:wght@300;400;600&family=Roboto:wght@400;500&display=swap">
<style>
  :root {
    --page-bg: #e9e6e1;
    --card-black: #0d0d0d;
    --card-graphite: #2e2e2e;
    --brand-red: #f04a22;
    --brand-red-deep: #c9261a;
    --text-white: #f4f4f4;
    --text-grey: #c9c9c9;
    --text-rose: #f2a89a;
    --logo-ink: #161616;
  }
  html, body {
    margin: 0;
    width: 1200px;
    height: 969px;
    overflow: hidden;
    background: var(--page-bg);
  }
  .card {
    position: absolute;
    left: 100px;
    top: 200px;
    width: 1000px;
    height: 570px;
    border-radius: 28px;
    overflow: hidden;
    box-shadow: 0 18px 40px rgba(0,0,0,0.25);
  }
  .card-art { position: absolute; inset: 0; }
  .trainer-name {
    position: absolute; left: 52px; top: 58px; margin: 0;
    font: 400 36px/1 "Oswald", sans-serif;
    color: var(--brand-red); letter-spacing: 0.5px;
  }
  .trainer-role {
    position: absolute; left: 52px; top: 108px; margin: 0;
    font: 500 25px/1 "Roboto", sans-serif; color: var(--text-white);
  }
  .contact-list {
    position: absolute; left: 52px; top: 320px; margin: 0; padding: 0;
    list-style: none;
    font: 400 24px/1 "Roboto", sans-serif; color: var(--text-white);
  }
  .contact-list li { display: flex; align-items: center; gap: 14px; height: 33px; }
  .contact-icon { width: 22px; height: 22px; flex: none; }
  .service-title {
    position: absolute; left: 52px; top: 400px; margin: 0;
    font: 500 22px/1 "Roboto", sans-serif; color: var(--brand-red);
  }
  .motto {
    position: absolute; left: 52px; top: 436px; margin: 0;
    font: 400 23px/31px "Roboto", sans-serif; color: var(--text-grey);
  }
  .motto em { font-style: normal; color: var(--text-rose); }
  .brand-name {
    position: absolute; left: 703px; top: 360px; transform: translateX(-50%);
    margin: 0; white-space: nowrap;
    font: 600 92px/1 "Oswald", sans-serif; color: var(--logo-ink);
  }
  .brand-sub {
    position: absolute; left: 703px; top: 470px; transform: translateX(-50%);
    margin: 0; white-space: nowrap;
    font: 300 24px/1 "Oswald", sans-serif; color: var(--logo-ink);
    text-transform: uppercase; letter-spacing: 0.5px;
  }
  .brand-dot {
    position: absolute; left: 653px; top: 200px;
    width: 100px; height: 100px; border-radius: 50%;
    background: var(--brand-red-deep);
  }
</style>
</head>
<body>
  <section class="card">
    <svg class="card-art" viewBox="0 0 1000 570" width="1000" height="570" aria-hidden="true">
      <defs>
        <linearGradient id="cardShade" x1="0" y1="0" x2="1" y2="0">
          <stop offset="0" stop-color="#1a1a1a"/>
          <stop offset="0.35" stop-color="#2a2a2a"/>
          <stop offset="0.6" stop-color="#111"/>
          <stop offset="0.78" stop-color="#5a1a12"/>
          <stop offset="1" stop-color="#e0321c"/>
        </linearGradient>
        <radialGradient id="frost" cx="0.45" cy="0.4" r="0.7">
          <stop offset="0" stop-color="#fbf7f3" stop-opacity="0.92"/>
          <stop offset="0.7" stop-color="#efe4dc" stop-opacity="0.85"/>
          <stop offset="1" stop-color="#e2cfc4" stop-opacity="0.8"/>
        </radialGradient>
      </defs>
      <rect width="1000" height="570" fill="url(#cardShade)"/>
      <circle cx="703" cy="324" r="293" fill="url(#frost)"/>
      <circle cx="703" cy="324" r="293" fill="none" stroke="#ffffff" stroke-opacity="0.5" stroke-width="2"/>
    </svg>

    <h1 class="trainer-name">DANIEL WHITCOMBE</h1>
    <p class="trainer-role">Personal Trainer</p>

    <ul class="contact-list">
      <li>
        <svg class="contact-icon" viewBox="0 0 24 24"><rect x="2" y="5" width="20" height="14" rx="2" fill="var(--brand-red)"/><path d="M3 6l9 7 9-7" fill="none" stroke="#1a1a1a" stroke-width="2"/></svg>
        dan@vek.example
      </li>
      <li>
        <svg class="contact-icon" viewBox="0 0 24 24"><circle cx="12" cy="12" r="10" fill="var(--brand-red)"/><path d="M2 12h20M12 2c3 3 3 17 0 20M12 2c-3 3-3 17 0 20" fill="none" stroke="#1a1a1a" stroke-width="1.6"/></svg>
        www.vek.example
      </li>
    </ul>

    <p class="service-title">Online Personal Training service</p>
    <p class="motto">Take control of your personal health<br>to unleash your <em>greatest potential</em></p>

    <span class="brand-dot"></span>
    <p class="brand-name">VEK.PRO</p>
    <p class="brand-sub">Daniel Whitcombe Fitness</p>
  </section>
</body>
</html>
```